Re-design my 1-page website to be BETTER!

Hi Guys,
I recently created a 1-page website for market testing purposes for a company I am starting. Problem is, the feedback i've had on the page is its a bit corporate and boring.
I would love you to design something that is fresher, more modern and will generate leads (via the sign up CTA's).
Here is the website as it is now: www.guidebridgehub.com.au.
If you need any info or have questions, just reach out.
Thanks,
Oliver

Target Market(s)

Entrepreneurs

Number of Pages Required

1 page

Font styles to use
Sans Serif

Colors
abd036
34a6d7
ffffff

Requirements
Must have
• Fresh, Modern, high-converting
• I expect 70% of traffic to be mobile so must be mobile optimised first.
Nice to have
• I've highlighted colours i like below, however, I am open to suggestions. I like colours that are gender neutral and show energy and vibrancy.
• I have used Proxima Nova for the fonts, as I find it easy to read however, I am open to suggestions. My main preference is that it displays well and is easily read

```html
<!DOCTYPE html>
<html lang="en">
<head>
<meta charset="utf-8">
<title>GuideBridge Hub – Mentorship But Different</title>
<link href="https://fonts.googleapis.com/css2?family=Lato:wght@300;400;700&display=swap" rel="stylesheet">
<style>
:root{
  --blue:#34a6d7;
  --blue-dark:#2a8fbc;
  --green:#abd036;
  --ink:#2f3a40;
  --text:#5b666c;
  --muted:#8a9398;
  --line:#dde2e5;
  --panel:#f4f6f7;
  --white:#ffffff;
  --hero-a:#3b3128;
  --hero-b:#8a6a4e;
}
*{box-sizing:border-box;margin:0;padding:0}
html,body{width:1200px;height:4244px;overflow:hidden}
body{font-family:"Lato",Arial,sans-serif;color:var(--text);background:var(--white);position:relative;font-size:15px;line-height:1.6}
.section{position:absolute;left:0;width:1200px}
.h2{font-weight:400;font-size:34px;color:var(--ink);text-align:center;letter-spacing:.2px}
.btn{display:inline-block;background:var(--blue);color:var(--white);font-size:13px;font-weight:700;letter-spacing:1px;padding:13px 28px;border-radius:3px;text-transform:uppercase}
.brand{font-size:30px;font-weight:400;color:var(--ink);letter-spacing:-.3px;line-height:1}

/* Hero */
.hero{top:0;height:820px;background:linear-gradient(120deg,var(--hero-a) 0%,var(--hero-b) 45%,#5a4636 75%,#2c2520 100%)}
.hero-photo{position:absolute;inset:0}
.topbar{position:absolute;top:0;left:0;width:1200px;height:70px;background:var(--white);display:flex;align-items:center;justify-content:space-between;padding:0 40px}
.nav{display:flex;align-items:center;gap:26px;font-size:13px;font-weight:700;color:var(--ink);letter-spacing:.5px}
.nav .btn{padding:10px 20px;font-size:12px}
.hero-copy{position:absolute;top:280px;left:0;width:1200px;text-align:center;color:var(--white)}
.hero-copy h1{font-size:54px;font-weight:300;letter-spacing:.5px}
.hero-copy p{font-size:22px;line-height:1.45;margin-top:14px}
.hero-actions{margin-top:44px;display:flex;justify-content:center;gap:22px}

/* About */
.about{top:880px;height:260px}
.about h2{position:absolute;left:60px;top:0;font-size:34px;font-weight:400;color:var(--ink)}
.about-text{position:absolute;left:60px;top:64px;width:660px;font-size:14px}
.about-text p{margin-bottom:14px}
.about-text .btn{margin-top:8px}
.about-media{position:absolute;left:800px;top:10px;width:340px;height:250px;background:linear-gradient(135deg,#6d5a4a,#a98b6c 50%,#4b3d33)}
.play{position:absolute;left:140px;top:95px}

/* How it works */
.how{top:1200px;height:320px}
.how .h2{margin-bottom:56px}
.steps{display:flex;justify-content:center;align-items:flex-start;padding:0 60px}
.step{width:300px}
.step h3{font-size:17px;font-weight:700;color:var(--ink);margin-top:12px}
.step p{font-size:13px;margin-top:6px}
.step-arrow{width:68px;display:flex;justify-content:center;padding-top:90px}

/* Testimonial */
.clients{top:1550px;height:300px;background:var(--white)}
.clients .h2{margin-bottom:40px}
.quote{width:860px;margin:0 auto;text-align:center;font-size:22px;font-weight:300;font-style:italic;color:var(--text);line-height:1.5}
.author{text-align:center;margin-top:24px;font-size:14px;font-weight:700;color:var(--ink)}
.author span{display:block;font-weight:400;font-size:12px;color:var(--muted)}
.car{position:absolute;top:108px}

/* Accelerate */
.growth{top:1880px;height:800px}
.growth .h2{margin-bottom:44px}
.grid{display:grid;grid-template-columns:470px 470px;gap:26px 40px;justify-content:center}
.card{border:1px solid var(--line);height:170px;background:var(--white)}
.card h3{background:var(--panel);border-bottom:1px solid var(--line);font-size:16px;font-weight:700;color:var(--ink);padding:12px 18px}
.card p{font-size:13px;padding:12px 18px;line-height:1.55}
.growth-cta{text-align:center;margin-top:48px}
.growth-cta small{display:block;margin-top:12px;font-size:12px;color:var(--muted)}

/* FAQ */
.faq{top:2700px;height:830px}
.faq .h2{margin-bottom:38px}
.faq-list{width:880px;margin:0 auto}
.faq-item{border:1px solid var(--line);height:58px;display:flex;align-items:center;gap:16px;padding:0 18px;margin-bottom:14px;font-size:16px;color:var(--ink);box-shadow:0 2px 4px rgba(0,0,0,.05)}
.faq-answer{font-size:13px;padding:2px 18px 18px}
.faq-answer p{margin-bottom:12px}

/* Invest */
.invest{top:3560px;height:350px}
.invest-card{width:1080px;height:340px;margin:0 auto;background:var(--panel);text-align:center;padding-top:70px}
.invest-card h2{font-size:32px;font-weight:400;color:var(--ink)}
.invest-card p{font-size:14px;width:560px;margin:10px auto 22px}
.invest-card small{display:block;margin-top:12px;font-size:12px;color:var(--muted)}

/* Footer */
.footer{top:3990px;height:254px}
.footer-top{display:flex;justify-content:space-between;align-items:flex-start;padding:0 60px;height:100px}
.subscribe h4{font-size:15px;font-weight:400;color:var(--ink);margin-bottom:10px}
.subscribe-row{display:flex;gap:12px}
.subscribe-input{width:260px;height:40px;border-bottom:1px solid var(--line);font-size:13px;color:var(--muted);padding-top:10px}
.subscribe-btn{height:40px;border:1px solid var(--blue);color:var(--blue);font-size:13px;padding:10px 22px;border-radius:3px}
.footer-links{display:flex;justify-content:center;gap:28px;font-size:12px;font-weight:700;color:var(--ink);letter-spacing:.5px;margin-top:36px}
.footer-bottom{position:absolute;bottom:0;left:0;width:1200px;height:56px;border-top:1px solid var(--line);display:flex;align-items:center;justify-content:space-between;padding:0 60px;font-size:12px;color:var(--muted)}
.socials{display:flex;gap:10px}
.socials span{width:18px;height:18px;border-radius:50%;background:#b5bcc0;display:block}
</style>
</head>
<body>

<header class="section hero">
  <div class="hero-photo" role="img" aria-label="Photo of a mentor and entrepreneur talking in a warm-lit cafe"></div>
  <div class="topbar">
    <div class="brand">GuideBridge Hub</div>
    <nav class="nav">
      <span>ABOUT</span><span>HOW IT WORKS</span><span>FAQ</span><span>CONTACT</span>
      <span class="btn">Get Started</span>
    </nav>
  </div>
  <div class="hero-copy">
    <h1>Mentorship But Different</h1>
    <p>Finding a Mentor used to be hard, but not any more.<br>We've turned the traditional model on its head, so now Mentors seek you.</p>
    <div class="hero-actions"><span class="btn">Learn More</span><span class="btn">Register Now</span></div>
  </div>
</header>

<section class="section about">
  <h2>About GuideBridge Hub</h2>
  <div class="about-text">
    <p>Having a great Mentor will turbo charge your personal, professional or business growth. But unless you have an incredible network, finding great Mentors has always been a challenge.</p>
    <p>GuideBridge Hub changes all that, levelling the playing field and making it easy for entrepreneurs and professionals to find the advice and guidance they deserve.</p>
    <p>No longer will you have to go searching for your perfect Mentor. We bring the perfect Mentor to you, selected from a global pool of experts, putting the power back in your hands and letting you get on with your growth.</p>
    <span class="btn">Let's Get Started</span>
  </div>
  <div class="about-media" role="img" aria-label="Video still of a group of young professionals chatting in an office">
    <svg class="play" width="60" height="60" viewBox="0 0 60 60"><circle cx="30" cy="30" r="30" fill="#34a6d7"/><path d="M24 18 L42 30 L24 42Z" fill="#fff"/></svg>
  </div>
</section>

<section class="section how">
  <h2 class="h2">How It Works</h2>
  <div class="steps">
    <div class="step">
      <svg width="56" height="46" viewBox="0 0 56 46" fill="none" stroke="#2f3a40" stroke-width="2"><circle cx="16" cy="12" r="8"/><path d="M2 44c0-9 6-16 14-16s14 7 14 16"/><path d="M34 4h20v14h-12l-6 5v-5h-2z" stroke="#34a6d7"/></svg>
      <h3>Tell Us What You Need</h3>
      <p>There is no one size fits all approach to Mentorship. So tell us the challenges you are facing and the skills and experience you want.</p>
    </div>
    <div class="step-arrow"><svg width="22" height="22" viewBox="0 0 22 22"><circle cx="11" cy="11" r="11" fill="#2f3a40"/><path d="M9 6l5 5-5 5" stroke="#fff" stroke-width="2" fill="none"/></svg></div>
    <div class="step">
      <svg width="46" height="46" viewBox="0 0 46 46" fill="none" stroke="#2f3a40" stroke-width="2"><circle cx="23" cy="12" r="9"/><path d="M6 44c0-10 7-18 17-18s17 8 17 18"/><path d="M23 26v10" stroke="#34a6d7"/></svg>
      <h3>Choose Your Mentor</h3>
      <p>We match you with Mentors who suit your criteria. It's then up to you whether you choose a Mentor, interview a few or simply start a chat.</p>
    </div>
    <div class="step-arrow"><svg width="22" height="22" viewBox="0 0 22 22"><circle cx="11" cy="11" r="11" fill="#2f3a40"/><path d="M9 6l5 5-5 5" stroke="#fff" stroke-width="2" fill="none"/></svg></div>
    <div class="step">
      <svg width="56" height="46" viewBox="0 0 56 46" fill="none" stroke="#2f3a40" stroke-width="2"><circle cx="16" cy="12" r="8"/><circle cx="40" cy="12" r="8"/><path d="M2 44c0-9 6-16 14-16 5 0 9 2 12 6 3-4 7-6 12-6 8 0 14 7 14 16"/></svg>
      <h3>Ongoing Support</h3>
      <p>We don't stop once you have found your perfect Mentor. We're on hand to make sure you keep your sessions on track and offer ongoing support.</p>
    </div>
  </div>
</section>

<section class="section clients">
  <h2 class="h2">What Our Clients Say</h2>
  <svg class="car" style="left:100px" width="16" height="28" viewBox="0 0 16 28"><path d="M14 2 L3 14 L14 26" stroke="#34a6d7" stroke-width="2.5" fill="none"/></svg>
  <svg class="car" style="left:1084px" width="16" height="28" viewBox="0 0 16 28"><path d="M2 2 L13 14 L2 26" stroke="#34a6d7" stroke-width="2.5" fill="none"/></svg>
  <p class="quote">" Donec mi sapien, congue eu massa vel, elementum volutpat justo ullamcorper diam gravida. Proin luctus eleifend nisl non luctus."</p>
  <p class="author">Tara Lindqvist<span>Customer</span></p>
</section>

<section class="section growth">
  <h2 class="h2">Accelerate Your Growth</h2>
  <div class="grid">
    <div class="card"><h3>Impartial advice</h3><p>Imagine being able to speak to someone who has been through the challenges you are currently facing. Who has been there and done that and can help you navigate the ups and downs of your career or business.</p></div>
    <div class="card"><h3>Avoid the Pitfalls</h3><p>An experienced Mentor will help you see the challenges before they arise and make sure you avoid them altogether. Saving valuable time and money in the process.</p></div>
    <div class="card"><h3>A Supportive Ear</h3><p>Running a business and the challenges of corporate life can be extremely stressful. And often, our friends and family just don't get it. An impartial Mentor understands what you are going through and helps you see things objectively.</p></div>
    <div class="card"><h3>Clarity</h3><p>Sometimes we are so caught up in our own world we struggle to see the big picture. Your Mentor will provide an objective, outside view, helping you to cut through the noise and focus on what really matters.</p></div>
    <div class="card"><h3>Motivation</h3><p>Your Mentor has seen the highs and lows before. They understand what you are going through and will help you to stay focused and keep moving forward with energy.</p></div>
    <div class="card"><h3>Make you Accountable</h3><p>A Mentor is not just there to pat you on the back. They will set goals with you and hold you to them when things slip. Ultimately, only you can control your success, and your Mentor will help you get there.</p></div>
  </div>
  <div class="growth-cta"><span class="btn">Register Now</span><small>100% confidential and obligation free.</small></div>
</section>

<section class="section faq">
  <h2 class="h2">Frequently Asked Questions</h2>
  <div class="faq-list">
    <div class="faq-item"><svg width="22" height="22" viewBox="0 0 22 22"><circle cx="11" cy="11" r="11" fill="#34a6d7"/><path d="M11 6v10M6 11h10" stroke="#fff" stroke-width="2"/></svg>What is a Mentor?</div>
    <div class="faq-item"><svg width="22" height="22" viewBox="0 0 22 22"><circle cx="11" cy="11" r="11" fill="#34a6d7"/><path d="M6 11h10" stroke="#fff" stroke-width="2"/></svg>Is a Mentor right for me?</div>
    <div class="faq-answer">
      <p>If you have a desire to succeed, a willingness to listen and learn, and the drive to challenge yourself and work on continuous improvement, then yes. A Mentor is perfect for you.</p>
      <p>If you want the inside line, if you want to cut down the learning curve and accelerate your business, professional or personal growth, then yes. A Mentor is perfect for you.</p>
      <p>A great Mentor will not only focus on your strengths, but help you identify your weaknesses. If you find the thought of this too confronting, perhaps a Mentor is not right for you.</p>
    </div>
    <div class="faq-item"><svg width="22" height="22" viewBox="0 0 22 22"><circle cx="11" cy="11" r="11" fill="#34a6d7"/><path d="M11 6v10M6 11h10" stroke="#fff" stroke-width="2"/></svg>How often do we meet?</div>
    <div class="faq-item"><svg width="22" height="22" viewBox="0 0 22 22"><circle cx="11" cy="11" r="11" fill="#34a6d7"/><path d="M11 6v10M6 11h10" stroke="#fff" stroke-width="2"/></svg>Can I have more than one Mentor?</div>
    <div class="faq-item"><svg width="22" height="22" viewBox="0 0 22 22"><circle cx="11" cy="11" r="11" fill="#34a6d7"/><path d="M11 6v10M6 11h10" stroke="#fff" stroke-width="2"/></svg>What if it doesn't work out?</div>
    <div class="faq-item"><svg width="22" height="22" viewBox="0 0 22 22"><circle cx="11" cy="11" r="11" fill="#34a6d7"/><path d="M11 6v10M6 11h10" stroke="#fff" stroke-width="2"/></svg>How do we meet?</div>
    <div class="faq-item"><svg width="22" height="22" viewBox="0 0 22 22"><circle cx="11" cy="11" r="11" fill="#34a6d7"/><path d="M11 6v10M6 11h10" stroke="#fff" stroke-width="2"/></svg>What are the costs?</div>
  </div>
</section>

<section class="section invest">
  <div class="invest-card">
    <h2>It's Time to Invest in You</h2>
    <p>If you've come this far you've already taken the most important step, recognising how mentorship can help you. Let's bring a Mentor to you.</p>
    <span class="btn">Get Started Now</span>
    <small>And let the right Mentor find you</small>
  </div>
</section>

<footer class="section footer">
  <div class="footer-top">
    <div class="brand">GuideBridge Hub</div>
    <div class="subscribe">
      <h4>Subscribe To Our Newsletter</h4>
      <div class="subscribe-row"><div class="subscribe-input">Email Address</div><div class="subscribe-btn">Subscribe</div></div>
    </div>
  </div>
  <div class="footer-links"><span>ABOUT</span><span>HOW IT WORKS</span><span>FAQ</span><span>CONTACT</span></div>
  <div class="footer-bottom">
    <span>© 2018 GuideBridgeHub.com</span>
    <div class="socials"><span></span><span></span><span></span></div>
  </div>
</footer>

</body>
</html>
```